Design for an iOS and Android app managing shopping list

The app allows you to keep manage shopping lists, each shopping list being made of items to buy...
We need a design for the 3 screens of the app:
a) global view showing list of (shopping) list
b) form enabling to edit the name of a (shopping) list
c) detailed view listing the contents/items of a (shopping) list
d) 1 text page [not illustrated]
2 "alerts" items are also to be designed: confirm and error pop ups.
No specific guidelines, nor logo or whatever.
It will be a free app distributed on iOS and Androïd.
We just want to make it looking nice & very usable for end users.

```html
<!DOCTYPE html>
<html lang="fr">
<head>
<meta charset="utf-8">
<title>Shopping Lists – App Screens</title>
<link rel="stylesheet" href="https://fonts.googleapis.com/css2?family=Source+Sans+3:ital,wght@0,400;0,600;0,700;1,700&display=swap">
<style>
:root{
  --bg:#e4e5ea;
  --status:#2f3c8f;
  --primary:#3d4db7;
  --primary-text:#ffffff;
  --tint:#e6e8f6;
  --tint-text:#3d4db7;
  --surface:#ffffff;
  --divider:#e3e3e8;
  --text:#3a3a42;
  --icon:#a3a3ab;
  --nav:#000000;
  --accent:#e91e63;
  --pending:#ff9800;
  --done:#4caf50;
  --key-bg:#eceff1;
  --key:#ffffff;
}
*{box-sizing:border-box;margin:0;padding:0}
html,body{width:705px;height:1200px;overflow:hidden}
body{background:var(--bg);font-family:"Source Sans 3",Arial,sans-serif;color:var(--text)}
.board{display:grid;grid-template-columns:320px 320px;grid-template-rows:567px 567px;gap:25px;padding:20px}
.screen{position:relative;display:flex;flex-direction:column;background:var(--surface);overflow:hidden;box-shadow:0 2px 8px rgba(0,0,0,.18)}
.status-bar{height:18px;background:var(--status);color:#fff;font-size:8px;display:flex;align-items:center;justify-content:space-between;padding:0 8px}
.status-bar .icons{display:flex;gap:4px;align-items:center}
.status-bar .icons span{display:block;width:8px;height:6px;background:#fff;border-radius:1px}
.app-bar{height:38px;background:var(--primary);color:var(--primary-text);display:flex;align-items:center;gap:10px;padding:0 12px;font-size:13px;font-weight:600;letter-spacing:.4px}
.content{flex:1;display:flex;flex-direction:column;background:var(--surface)}
.add-row{height:34px;background:var(--tint);display:flex;align-items:center;justify-content:space-between;padding:0 12px;color:var(--tint-text);font-size:11px;font-weight:700;font-style:italic}
.add-row .plus{font-style:normal;font-size:18px;font-weight:600}
.list-row{height:34px;display:flex;align-items:center;justify-content:space-between;padding:0 12px;border-bottom:1px solid var(--divider);font-size:11px}
.trash{width:11px;height:12px;fill:var(--icon)}
.spacer{flex:1}
.about-bar{height:26px;background:var(--tint);color:var(--tint-text);font-size:9px;font-weight:700;display:flex;align-items:center;justify-content:center;letter-spacing:.5px}
.nav-bar{height:34px;background:var(--nav);display:flex;align-items:center;justify-content:space-around;padding:0 40px}
.nav-bar svg{width:14px;height:14px;fill:none;stroke:#fff;stroke-width:1.6}
.scrim{position:absolute;left:0;right:0;top:18px;bottom:34px;background:rgba(20,20,30,.62)}
.dialog{position:absolute;left:45px;right:45px;top:215px;background:var(--surface);border-radius:3px;padding:14px 14px 10px;text-align:center;box-shadow:0 6px 18px rgba(0,0,0,.4)}
.dialog .big-trash{width:30px;height:34px;fill:#111}
.dialog h2{font-size:11px;font-weight:700;letter-spacing:.3px;margin-top:6px;color:#222}
.dialog p{font-size:9.5px;color:#666;margin-top:3px;line-height:1.25}
.dialog .actions{display:flex;justify-content:space-around;margin-top:12px;font-size:9px;font-weight:700;color:var(--tint-text);letter-spacing:.4px}
.app-bar .back{width:14px;height:14px;fill:none;stroke:#fff;stroke-width:2}
.form{padding:22px 16px 0}
.field{height:40px;border:2px solid var(--primary);border-radius:6px;background:var(--tint);display:flex;align-items:center;padding:0 12px;font-size:11px;font-weight:700;font-style:italic;color:var(--tint-text)}
.save-button{margin-top:10px;height:32px;border-radius:16px;background:var(--accent);color:#fff;font-size:11px;font-weight:700;letter-spacing:.6px;display:flex;align-items:center;justify-content:center}
.keyboard{margin-top:auto;background:var(--key-bg);padding:8px 4px 6px;display:flex;flex-direction:column;gap:9px}
.key-row{display:flex;justify-content:center;gap:4px}
.key{width:27px;height:26px;display:flex;align-items:center;justify-content:center;font-size:12px;color:#333}
.key.wide{width:40px;font-size:9px}
.key.space{width:130px;background:var(--key);border-radius:3px;font-size:8px;color:#888}
.key.enter{width:24px;height:24px;border-radius:50%;background:var(--primary);color:#fff;font-size:11px}
.section{height:20px;display:flex;align-items:center;padding:0 12px;color:#fff;font-size:8.5px;font-weight:700;letter-spacing:.6px}
.section.pending{background:var(--pending)}
.section.done{background:var(--done)}
.item-label{display:flex;align-items:center;gap:10px}
.check{width:13px;height:13px;border:1.6px solid var(--pending);border-radius:2px;background:#fff}
.check.ticked{border-color:var(--done);display:flex;align-items:center;justify-content:center}
.check.ticked svg{width:9px;height:9px;fill:none;stroke:var(--done);stroke-width:2.4}
</style>
</head>
<body>
<svg width="0" height="0" style="position:absolute" aria-hidden="true">
  <symbol id="icon-trash" viewBox="0 0 22 24"><rect x="0" y="2" width="22" height="3" rx="1"/><rect x="8" y="0" width="6" height="3"/><path d="M2 7h18l-1.6 17H3.6z"/></symbol>
  <symbol id="icon-tick" viewBox="0 0 10 10"><path d="M1 5.2l2.6 2.6L9 2"/></symbol>
</svg>

<main class="board">

  <!-- Lists overview -->
  <section class="screen">
    <div class="status-bar"><span>Carrier</span><span>5:38PM</span><span class="icons"><span></span><span></span></span></div>
    <header class="app-bar">LISTS</header>
    <div class="content">
      <div class="add-row">Add a new shopping list<span class="plus">+</span></div>
      <div class="list-row">Diner de ce soir<svg class="trash"><use href="#icon-trash"/></svg></div>
      <div class="list-row">Course noel<svg class="trash"><use href="#icon-trash"/></svg></div>
      <div class="list-row">Courses Maison Nord<svg class="trash"><use href="#icon-trash"/></svg></div>
      <div class="list-row">Marché Vert<svg class="trash"><use href="#icon-trash"/></svg></div>
      <div class="list-row">Ménage<svg class="trash"><use href="#icon-trash"/></svg></div>
      <div class="list-row">Cadeaux de noel<svg class="trash"><use href="#icon-trash"/></svg></div>
      <div class="spacer"></div>
      <div class="about-bar">ABOUT US »</div>
    </div>
    <nav class="nav-bar"><svg viewBox="0 0 14 14"><path d="M11 2L3 7l8 5z"/></svg><svg viewBox="0 0 14 14"><circle cx="7" cy="7" r="5"/></svg><svg viewBox="0 0 14 14"><rect x="2.5" y="2.5" width="9" height="9"/></svg></nav>
  </section>

  <!-- Delete confirmation -->
  <section class="screen">
    <div class="status-bar"><span>Carrier</span><span>5:38PM</span><span class="icons"><span></span><span></span></span></div>
    <header class="app-bar">LISTS</header>
    <div class="content">
      <div class="add-row">Add a new shopping list<span class="plus">+</span></div>
      <div class="list-row">Diner de ce soir<svg class="trash"><use href="#icon-trash"/></svg></div>
      <div class="list-row">Course noel<svg class="trash"><use href="#icon-trash"/></svg></div>
      <div class="list-row">Courses Maison Nord<svg class="trash"><use href="#icon-trash"/></svg></div>
      <div class="list-row">Marché Vert<svg class="trash"><use href="#icon-trash"/></svg></div>
      <div class="list-row">Ménage<svg class="trash"><use href="#icon-trash"/></svg></div>
      <div class="list-row">Cadeaux de noel<svg class="trash"><use href="#icon-trash"/></svg></div>
      <div class="spacer"></div>
      <div class="about-bar">ABOUT US »</div>
    </div>
    <nav class="nav-bar"><svg viewBox="0 0 14 14"><path d="M11 2L3 7l8 5z"/></svg><svg viewBox="0 0 14 14"><circle cx="7" cy="7" r="5"/></svg><svg viewBox="0 0 14 14"><rect x="2.5" y="2.5" width="9" height="9"/></svg></nav>
    <div class="scrim"></div>
    <div class="dialog" role="dialog">
      <svg class="big-trash"><use href="#icon-trash"/></svg>
      <h2>REMOVE THE SHOPPING LIST</h2>
      <p>Would you like to delete the shopping list?</p>
      <div class="actions"><span>CANCEL</span><span>DELETE</span></div>
    </div>
  </section>

  <!-- Edit list name -->
  <section class="screen">
    <div class="status-bar"><span>Carrier</span><span>5:38PM</span><span class="icons"><span></span><span></span></span></div>
    <header class="app-bar"><svg class="back" viewBox="0 0 14 14"><path d="M13 7H2M7 2L2 7l5 5"/></svg>UPDATE LIST NAME</header>
    <div class="content">
      <div class="form">
        <div class="field">Dîner de ce soir</div>
        <div class="save-button">SAVE</div>
      </div>
      <div class="keyboard">
        <div class="key-row"><span class="key">q</span><span class="key">w</span><span class="key">e</span><span class="key">r</span><span class="key">t</span><span class="key">y</span><span class="key">u</span><span class="key">i</span><span class="key">o</span><span class="key">p</span></div>
        <div class="key-row"><span class="key">a</span><span class="key">s</span><span class="key">d</span><span class="key">f</span><span class="key">g</span><span class="key">h</span><span class="key">j</span><span class="key">k</span><span class="key">l</span></div>
        <div class="key-row"><span class="key">⇧</span><span class="key">z</span><span class="key">x</span><span class="key">c</span><span class="key">v</span><span class="key">b</span><span class="key">n</span><span class="key">m</span><span class="key">⌫</span></div>
        <div class="key-row"><span class="key wide">?123</span><span class="key">,</span><span class="key space">English (US)</span><span class="key">.</span><span class="key enter">›</span></div>
      </div>
    </div>
    <nav class="nav-bar"><svg viewBox="0 0 14 14"><path d="M3 4l4 5 4-5"/></svg><svg viewBox="0 0 14 14"><circle cx="7" cy="7" r="5"/></svg><svg viewBox="0 0 14 14"><rect x="2.5" y="2.5" width="9" height="9"/></svg></nav>
  </section>

  <!-- List detail -->
  <section class="screen">
    <div class="status-bar"><span>Carrier</span><span>5:38PM</span><span class="icons"><span></span><span></span></span></div>
    <header class="app-bar">LIST NAME</header>
    <div class="content">
      <div class="add-row">Add a new item<span class="plus">+</span></div>
      <div class="section pending">PENDING</div>
      <div class="list-row"><span class="item-label"><span class="check"></span>Serviettes</span><svg class="trash"><use href="#icon-trash"/></svg></div>
      <div class="list-row"><span class="item-label"><span class="check"></span>Oignons</span><svg class="trash"><use href="#icon-trash"/></svg></div>
      <div class="list-row"><span class="item-label"><span class="check"></span>Bougies</span><svg class="trash"><use href="#icon-trash"/></svg></div>
      <div class="list-row"><span class="item-label"><span class="check"></span>Airelles</span><svg class="trash"><use href="#icon-trash"/></svg></div>
      <div class="list-row"><span class="item-label"><span class="check"></span>Foie gras</span><svg class="trash"><use href="#icon-trash"/></svg></div>
      <div class="section done">DONE</div>
      <div class="list-row"><span class="item-label"><span class="check ticked"><svg><use href="#icon-tick"/></svg></span>Saumon fumé</span><svg class="trash"><use href="#icon-trash"/></svg></div>
      <div class="list-row"><span class="item-label"><span class="check ticked"><svg><use href="#icon-tick"/></svg></span>Huile d'olive</span><svg class="trash"><use href="#icon-trash"/></svg></div>
      <div class="spacer"></div>
    </div>
    <nav class="nav-bar"><svg viewBox="0 0 14 14"><path d="M11 2L3 7l8 5z"/></svg><svg viewBox="0 0 14 14"><circle cx="7" cy="7" r="5"/></svg><svg viewBox="0 0 14 14"><rect x="2.5" y="2.5" width="9" height="9"/></svg></nav>
  </section>

</main>
</body>
</html>
```